" Ortopedista, especialista em cirurgia do pé e tornozelo. Especialista em cirurgia minimamente invasiva, incluindo cirurgia percutânea do pé e artroscopia de tornozelo. "

```html
<!DOCTYPE html>
<html lang="pt-BR">
<head>
<meta charset="UTF-8">
<title>Dr. Rafael Mendes — Cartão de Visita</title>
<link rel="stylesheet" href="https://fonts.googleapis.com/css2?family=Montserrat:wght@400;500;600&display=swap">
<style>
  :root {
    --navy: #1f2a5c;
    --purple: #7a5fae;
    --lavender: #e7e1f2;
    --card: #ffffff;
    --stage: #ececef;
    --text: #2a2f4a;
  }
  * { margin: 0; padding: 0; box-sizing: border-box; }
  html, body { width: 1200px; height: 1200px; overflow: hidden; }
  body {
    background: var(--stage);
    font-family: "Montserrat", sans-serif;
    color: var(--text);
    position: relative;
  }
  .card {
    position: absolute;
    left: 150px;
    width: 900px;
    height: 500px;
    background: var(--card);
    border-radius: 36px;
    overflow: hidden;
    box-shadow: 0 6px 24px rgba(0,0,0,0.08);
  }
  .card--front { top: 70px; }
  .card--back { top: 630px; }

  /* front */
  .edge-bar {
    position: absolute;
    height: 7px;
    background: var(--navy);
  }
  .edge-bar--top { top: 34px; left: 0; width: 58%; }
  .edge-bar--bottom { bottom: 34px; right: 0; width: 58%; }
  .front-identity {
    position: absolute;
    inset: 0;
    display: flex;
    flex-direction: column;
    align-items: center;
    justify-content: center;
  }
  .brand-dot {
    width: 96px;
    height: 96px;
    border-radius: 50%;
    background: var(--purple);
    margin-bottom: 22px;
  }
  .brand-name {
    font-size: 58px;
    font-weight: 600;
    letter-spacing: 1px;
    color: var(--navy);
    text-transform: uppercase;
    line-height: 1;
  }
  .specialty {
    align-self: stretch;
    text-align: center;
    margin-top: 10px;
    color: var(--navy);
  }
  .specialty__field {
    display: block;
    font-size: 20px;
    font-weight: 500;
    letter-spacing: 3px;
    text-transform: uppercase;
    color: var(--purple);
    padding-left: 260px;
  }
  .specialty__focus {
    display: block;
    margin-top: 4px;
    font-size: 19px;
    font-weight: 500;
    letter-spacing: 2.5px;
    text-transform: uppercase;
  }

  /* back */
  .side-stripe {
    position: absolute;
    left: 0; top: 0; bottom: 0;
    width: 12px;
    background: var(--purple);
  }
  .back-header {
    position: absolute;
    left: 70px; top: 50px;
  }
  .back-header .brand-name { font-size: 34px; }
  .back-header .tagline {
    margin-top: 6px;
    font-size: 12px;
    letter-spacing: 1.6px;
    text-transform: uppercase;
    color: var(--purple);
    font-weight: 500;
  }
  .contact-list {
    position: absolute;
    left: 70px; top: 170px;
    list-style: none;
  }
  .contact-list li {
    display: flex;
    align-items: center;
    gap: 16px;
    font-size: 20px;
    line-height: 1.3;
    margin-bottom: 22px;
    color: var(--text);
  }
  .contact-list .icon {
    width: 34px; height: 34px;
    flex: none;
    border-radius: 50%;
    background: var(--purple);
    display: flex; align-items: center; justify-content: center;
  }
  .contact-list .icon svg { width: 18px; height: 18px; }
  .brand-mark {
    position: absolute;
    right: 90px; top: 110px;
    width: 280px; height: 280px;
    border-radius: 50%;
    background: var(--lavender);
  }
</style>
</head>
<body>
  <section class="card card--front" aria-label="Frente do cartão">
    <div class="edge-bar edge-bar--top"></div>
    <div class="front-identity">
      <div class="brand-dot"></div>
      <div class="brand-name">Dr. Rafael Mendes</div>
      <div class="specialty">
        <span class="specialty__field">Ortopedia</span>
        <span class="specialty__focus">Cirurgia do Pé e Tornozelo Minimamente Invasiva</span>
      </div>
    </div>
    <div class="edge-bar edge-bar--bottom"></div>
  </section>

  <section class="card card--back" aria-label="Verso do cartão">
    <div class="side-stripe"></div>
    <header class="back-header">
      <div class="brand-name">Dr. Rafael Mendes</div>
      <div class="tagline">Cirurgia do pé e tornozelo minimamente invasiva</div>
    </header>
    <ul class="contact-list">
      <li>
        <span class="icon"><svg viewBox="0 0 24 24" fill="#fff"><path d="M6.6 10.8a15.2 15.2 0 0 0 6.6 6.6l2.2-2.2c.3-.3.7-.4 1-.2 1.1.4 2.3.6 3.6.6.6 0 1 .4 1 1V20c0 .6-.4 1-1 1A17 17 0 0 1 3 4c0-.6.4-1 1-1h3.5c.6 0 1 .4 1 1 0 1.3.2 2.5.6 3.6.1.3 0 .7-.2 1z"/></svg></span>
        00 0000 0000
      </li>
      <li>
        <span class="icon"><svg viewBox="0 0 24 24" fill="none" stroke="#fff" stroke-width="2"><rect x="3" y="5" width="18" height="14" rx="2"/><path d="M3 7l9 6 9-6"/></svg></span>
        contato@rafaelmendes.com.br
      </li>
      <li>
        <span class="icon"><svg viewBox="0 0 24 24" fill="none" stroke="#fff" stroke-width="2"><circle cx="12" cy="12" r="9"/><path d="M3 12h18M12 3c3 3 3 15 0 18M12 3c-3 3-3 15 0 18"/></svg></span>
        www.rafaelmendes.com.br
      </li>
      <li>
        <span class="icon"><svg viewBox="0 0 24 24" fill="#fff"><path d="M12 2a7 7 0 0 0-7 7c0 5 7 13 7 13s7-8 7-13a7 7 0 0 0-7-7zm0 9.5A2.5 2.5 0 1 1 12 6.5a2.5 2.5 0 0 1 0 5z"/></svg></span>
        <span>Rua nome da rua 00, bairro<br>Cidade - estado - cep 00000-000</span>
      </li>
    </ul>
    <div class="brand-mark"></div>
  </section>
</body>
</html>
```